new letterhead for my brokergae company KeelBright, Complete Marine Brokerage

We need a new letterhead for our brokerage company called KeelBright. We are specialised in selling pleasure crafts (sailing and motoryachts). More info can be found at https://keelbright-example.com/en

I use this document for a quotation, a letter, sales agreement, selling instructions. I am looking for a cover page + a content page.

Th efollowing information needs to be in the header / footer; email, website, VAT number, Bank Account number, number chamber of ccomerce, registry number prav, General terms and conditions DQRT apply.

```html
<!DOCTYPE html>
<html lang="en">
<head>
<meta charset="utf-8">
<title>KeelBright Stationery — Cover and Letter Page</title>
<link rel="stylesheet" href="https://fonts.googleapis.com/css2?family=Jost:wght@300;400;500&family=Arimo:wght@400;700&display=swap">
<style>
  :root {
    --backdrop: #dcdcdc;
    --paper: #f3f3f4;
    --cover-dark: #333334;
    --brand-blue: #1b57a6;
    --bar-grey: #6d6d6f;
    --band-grey: #a8a8aa;
    --rule: #c9c9cc;
    --ink: #3a3a3c;
    --ink-soft: #6a6a6d;
    --ink-light: #f2f2f2;
    --photo-sky: #7fa3c4;
    --photo-sea: #1d3f6b;
    --photo-hull: #2a2c30;
  }
  * { margin: 0; padding: 0; box-sizing: border-box; }
  html, body { width: 1200px; height: 901px; overflow: hidden; }
  body {
    background: var(--backdrop);
    font-family: "Arimo", Arial, sans-serif;
    color: var(--ink);
    position: relative;
  }
  .page {
    position: absolute;
    top: 105px;
    width: 490px;
    height: 692px;
    background: var(--paper);
    overflow: hidden;
  }
  .cover { left: 82px; }
  .letter { left: 630px; }

  /* Cover */
  .cover-head {
    position: absolute; left: 0; top: 0; width: 100%; height: 275px;
    background: var(--cover-dark);
  }
  .cover-accent {
    position: absolute; left: 32px; top: 0; width: 226px; height: 9px;
    background: var(--brand-blue);
  }
  .cover-title {
    position: absolute; left: 40px; top: 100px;
    font-family: "Jost", sans-serif; font-weight: 300;
    font-size: 40px; line-height: 42px; letter-spacing: 0.3px;
    color: var(--brand-blue);
  }
  .cover-project {
    position: absolute; left: 41px; top: 193px;
    font-size: 10px; line-height: 12.5px; color: var(--ink-light);
  }
  .cover-meta {
    position: absolute; right: 42px; top: 102px;
    text-align: right; color: var(--ink-light);
    font-size: 7px; line-height: 8.8px;
  }
  .cover-meta .label { font-weight: 700; }
  .cover-meta .client { font-size: 10px; line-height: 11px; }
  .cover-meta .block { margin-bottom: 9px; }
  .cover-photo {
    position: absolute; left: 0; top: 275px; width: 100%; height: 270px;
    background: linear-gradient(180deg, var(--photo-sky) 0%, #5f86ad 30%, var(--photo-hull) 58%, var(--photo-sea) 72%, #2c5585 100%);
  }
  .cover-footer {
    position: absolute; left: 0; top: 545px; width: 100%; height: 106px;
  }
  .brand {
    position: absolute;
    font-family: "Jost", sans-serif; font-weight: 400;
    color: var(--brand-blue);
    display: flex; align-items: center; gap: 8px;
  }
  .brand-dot { width: 14px; height: 14px; border-radius: 50%; background: var(--brand-blue); }
  .brand-name { font-size: 26px; line-height: 28px; }
  .brand-tag {
    position: absolute;
    font-family: "Jost", sans-serif; font-weight: 500;
    font-size: 6px; letter-spacing: 1.6px; color: var(--brand-blue);
  }
  .cover-footer .brand { left: 44px; top: 44px; }
  .cover-footer .brand-tag { left: 109px; top: 77px; }
  .contact {
    position: absolute; text-align: right;
    font-size: 7.2px; line-height: 10px; color: var(--ink);
  }
  .contact .key, .contact .domain { color: var(--brand-blue); font-weight: 700; }
  .cover-footer .contact { right: 42px; top: 48px; }
  .registration {
    position: absolute; left: 42px; right: 42px; top: 92px;
    font-size: 5.6px; line-height: 7px; color: var(--ink-soft);
    text-align: right;
  }
  .confidentiality {
    position: absolute; left: 0; top: 651px; width: 100%; height: 41px;
    background: var(--band-grey); color: #f4f4f4;
    padding: 7px 42px 0 42px; font-size: 5.8px; line-height: 7.6px;
  }
  .confidentiality strong { display: block; }

  /* Letter page */
  .letter-bar-blue { position: absolute; left: 0; top: 0; width: 294px; height: 6px; background: var(--brand-blue); }
  .letter-bar-grey { position: absolute; left: 298px; top: 0; width: 192px; height: 6px; background: var(--bar-grey); }
  .letter .brand { left: 39px; top: 45px; }
  .letter .brand-tag { left: 95px; top: 76px; }
  .letter .contact { right: 38px; top: 54px; font-size: 6.4px; line-height: 8.7px; }
  .letter-body {
    position: absolute; left: 38px; top: 187px; width: 414px;
    font-size: 6.8px; line-height: 8.7px; text-align: justify;
  }
  .letter-date { margin-bottom: 9px; }
  .recipient { margin-bottom: 55px; }
  .letter-body p { margin-bottom: 8.5px; }
  .closing { margin-top: 13px; display: flex; align-items: flex-start; gap: 10px; }
  .signature {
    width: 78px; height: 34px;
    background: linear-gradient(90deg, rgba(62,80,170,0.08), rgba(62,80,170,0.22), rgba(62,80,170,0.08));
    border-radius: 4px;
  }
  .letter-footer {
    position: absolute; left: 38px; right: 38px; top: 650px;
    border-top: 0.75px solid var(--rule);
    padding-top: 6px;
    display: flex; justify-content: space-between;
    font-size: 5.8px; line-height: 7.6px; color: var(--ink-soft);
  }
  .letter-footer .key { color: var(--brand-blue); font-weight: 700; }
  .letter-footer .terms { text-align: right; }
</style>
</head>
<body>

<section class="page cover">
  <div class="cover-head">
    <div class="cover-accent"></div>
    <h1 class="cover-title">BUSINESS<br>PROPOSAL</h1>
    <div class="cover-project">Project #125<br>Copper Gull Brand &amp; Website</div>
    <div class="cover-meta">
      <div class="block">
        <div class="label">Prepared for:</div>
        <div class="client">Daniel Corvey</div>
      </div>
      <div class="block">
        Copper Gull LLC<br>
        45 Harbour Ln, Port Town, 4100<br>
        P: 1300 555 010 · E hello@coppergull-example.com
      </div>
      <div class="block">
        <div class="label">Proposal Issued:</div>
        11.11.2017
      </div>
      <div class="block">
        <div class="label">Proposal Valid to:</div>
        01.12.2017
      </div>
    </div>
  </div>

  <div class="cover-photo" role="img" aria-label="Photograph of a dark-sailed yacht cutting through deep blue sea under a clear sky"></div>

  <div class="cover-footer">
    <div class="brand"><span class="brand-dot"></span><span class="brand-name">KeelBright</span></div>
    <div class="brand-tag">COMPLETE MARINE BROKERAGE</div>
    <div class="contact">
      Havenkade 12, 1011 AB Zeestad<br>
      <span class="key">T:</span> +31 20 555 01 28 · <span class="key">E:</span> info@keelbright-example.com<br>
      www.<span class="domain">keelbright-example</span>.com
    </div>
    <div class="registration">
      VAT NL000000000B01 · IBAN NL00 BANK 0000 0000 00 · CoC 00000000 · prav reg. no. 0000 · General terms and conditions DQRT apply
    </div>
  </div>

  <div class="confidentiality">
    <strong>Statement of Confidentiality</strong>
    This proposal and supporting materials contain confidential and proprietary business information of Brightline Studio. These materials may be printed or
    photocopied for use in evaluating the proposed project, but are not to be shared with other parties.
  </div>
</section>

<section class="page letter">
  <div class="letter-bar-blue"></div>
  <div class="letter-bar-grey"></div>
  <div class="brand"><span class="brand-dot"></span><span class="brand-name">KeelBright</span></div>
  <div class="brand-tag">COMPLETE MARINE BROKERAGE</div>
  <div class="contact">
    Havenkade 12, 1011 AB Zeestad<br>
    <span class="key">T:</span> +31 20 555 01 28 · <span class="key">E:</span> info@keelbright-example.com<br>
    www.<span class="domain">keelbright-example</span>.com
  </div>

  <div class="letter-body">
    <div class="letter-date">30.09.2017</div>
    <div class="recipient">Recipient’s name<br>Uferweg 7<br>20459 Hafenstadt<br>Germany</div>
    <p>Dear sir,</p>
    <p>Communication is a very integral part of living creatures, animals and humans. Communication may be verbal or written. Written communication however is only applicable to human beings. Can you even imagine a world without communication? Verbal communication can be through telephones, webcams or in person. Written communication is through letters, emails and mobile phone messages.</p>
    <p>In today’s world of great inventions and technology, letters have somehow become redundant. It is the time for text messages or chats. But they still can communicate a lot more than all other modes of communication. Organizations and various government departments still bank on letters as a strong medium of communication. There is no comparison in costs of sending letters as compared to costs of mobile phone messages though – letters are far cheaper. Letters now commonly known as “hard copy documents” are considered more relevant and important than email copies of text messages as proof or evidence of some sort.</p>
    <p>Letters speak volumes about a person or an organization that writes it. So one must take utmost care ensuring that the language used in any letter is appropriate for the occasion for which it is being written. Since a letter is also a written proof or document, if there are certain things that should not form a part of it, then that too should be carefully handled.</p>
    <p>Writing a good letter is an art. But if for some reason someone is unable to write that perfect letter, these different types of letters provide a base for you to build on. Sample letters have been given for everyone to understand what all information needs to form a part of the letter type and then it can be customized.</p>
    <div class="closing">
      <div>Yours Sincerely,<br>Lena Morvik</div>
      <div class="signature" role="img" aria-label="Handwritten signature in blue ink"></div>
    </div>
  </div>

  <footer class="letter-footer">
    <div>
      <span class="key">VAT:</span> NL000000000B01 · <span class="key">IBAN:</span> NL00 BANK 0000 0000 00<br>
      <span class="key">CoC:</span> 00000000 · <span class="key">prav reg. no.:</span> 0000
    </div>
    <div class="terms">
      info@keelbright-example.com · www.keelbright-example.com<br>
      General terms and conditions DQRT apply
    </div>
  </footer>
</section>

</body>
</html>
```